P.L.U.S.O.N. Content Framework Infographic

I am looking to take my basic infographic to the next level. I need to to translate the content marketing concept that is outlined in the uploaded file. I have attached the content and the image I would like used. I am not stuck on the colors represented in the image but do want to see a variety of options.

Target Market(s)

Companies that are looking for a content marketing strategy, SEO Agencies, marketing agencies

Industry/Entity Type

Digital marketing, SEO

Font styles to use
Other font styles liked:
• arial, calibri are fine

Colors
0054AA
0677BA
7BADD7
CADEEF
E8F1F8
0094D4
00A9DD
6FCCEA
C7EBF8
E9F6FB
00AB8E
00BBA5
67D7C9
C6EFE9
E9F9F6
59FF00
82FF00
B8FF75
E3FFCB
F4FFEA
EE7325
F08F49
F5BC92
FAE3D3
FDF4ED
EB3D1F
EC4F4E
F09395
F8D3D4
FCEDEE

Requirements
Must have
• The image that I provided with the content breakdown with section connectors to the image
Nice to have
• a few different way to present the data

```html
<!DOCTYPE html>
<html lang="en">
<head>
<meta charset="utf-8">
<title>P.L.U.S.O.N. Content Framework</title>
<link href="https://fonts.googleapis.com/css2?family=Lato:wght@400;700&display=swap" rel="stylesheet">
<style>
  :root {
    --page-bg: #ffffff;
    --panel-bg: #f5f5f5;
    --ink: #111111;
    --accent: #ec4f4e;
    --rule: #000000;
    --multimedia-head: #7badd7;
    --multimedia-body: #e8f1f8;
    --multimedia-line: #0677ba;
    --engagement-head: #b8ff75;
    --engagement-body: #f4ffea;
    --engagement-line: #59ff00;
    --expertise-head: #f5bc92;
    --expertise-body: #fdf4ed;
    --expertise-line: #ee7325;
    --experience-head: #f09395;
    --experience-body: #fcedee;
    --experience-line: #eb3d1f;
    --authority-head: #67d7c9;
    --authority-body: #e9f9f6;
    --authority-line: #00ab8e;
    --trust-head: #6fccea;
    --trust-body: #e9f6fb;
    --trust-line: #0094d4;
  }
  * { box-sizing: border-box; margin: 0; padding: 0; }
  html, body {
    width: 835px; height: 1200px; overflow: hidden;
    background: var(--page-bg);
    font-family: "Lato", Arial, sans-serif;
    color: var(--ink);
  }
  .panel {
    position: absolute; left: 42px; top: 45px;
    width: 747px; height: 1115px;
    background: var(--panel-bg);
  }
  .title {
    position: absolute; left: 0; right: 0; top: 50px;
    text-align: center; font-size: 15px; font-weight: 700;
  }
  .title .brand { color: var(--accent); font-weight: 400; }
  .intro {
    position: absolute; left: 82px; top: 93px; width: 588px;
    font-size: 10px; line-height: 16.4px;
  }
  .hero-figure {
    position: absolute; left: 188px; top: 245px;
    width: 400px; height: 210px;
    border-radius: 46% 50% 38% 42% / 40% 44% 46% 50%;
    background: linear-gradient(90deg, #f5bc92 0%, #6fccea 25%, #67d7c9 42%, #7badd7 58%, #f09395 74%, #b8ff75 100%);
  }
  .connectors {
    position: absolute; left: 0; top: 0;
    width: 747px; height: 1115px;
    pointer-events: none;
  }
  .connectors polyline { fill: none; stroke-width: 1.5; }
  .breakdown {
    position: absolute; left: 82px; top: 506px; width: 596px;
    border: 1.5px solid var(--rule);
  }
  .pillar + .pillar { border-top: 1.5px solid var(--rule); }
  .pillar-name {
    height: 27px; padding: 0 12px;
    font-size: 9.8px; font-weight: 700; line-height: 27px;
  }
  .pillar-text {
    padding: 6px 12px 0;
    font-size: 10px; line-height: 16.4px;
  }
  .multimedia .pillar-name { background: var(--multimedia-head); }
  .multimedia .pillar-text { background: var(--multimedia-body); height: 66px; }
  .engagement .pillar-name { background: var(--engagement-head); }
  .engagement .pillar-text { background: var(--engagement-body); height: 66px; }
  .expertise .pillar-name { background: var(--expertise-head); }
  .expertise .pillar-text { background: var(--expertise-body); height: 51px; }
  .experience .pillar-name { background: var(--experience-head); }
  .experience .pillar-text { background: var(--experience-body); height: 66px; }
  .authority .pillar-name { background: var(--authority-head); }
  .authority .pillar-text { background: var(--authority-body); height: 66px; line-height: 15px; }
  .trust .pillar-name { background: var(--trust-head); }
  .trust .pillar-text { background: var(--trust-body); height: 80px; line-height: 15px; }
</style>
</head>
<body>
<main class="panel">
  <h1 class="title">Putting <span class="brand">P.L.U.S.O.N.</span> on the bone for the User &amp; Searchly To Chew on</h1>
  <p class="intro">In SEO content is still king.&nbsp; What has changed with content is not the content but the delivery of that content.&nbsp; People these days are consuming content in so many different places &amp; formats that it makes it difficult to create engaging content that ranks and converts.&nbsp; Some people prefer to continue reading webpages to find the information they are looking for.&nbsp; Some prefer to see the pictures because they are more visual than contextual.&nbsp; Others would prefer to just watch video on ClipTube or other online video platforms, and in some cases it is more of an auditory way such as podcast &amp; streaming radio platforms.&nbsp; This infographic will breakdown how all of the pieces fit together to get “P.L.U.S.O.N” on the bone of content.</p>

  <div class="hero-figure" role="img" aria-label="Illustration of a pig divided into butcher-style cuts labelled Expertise, Trust, Multimedia, Authori, Experience and Engagement"></div>

  <svg class="connectors" viewBox="0 0 747 1115" aria-hidden="true">
    <polyline points="215,425 215,470 14,470 14,973 82,973" stroke="var(--trust-line)"/>
    <circle cx="215" cy="425" r="3.5" fill="var(--trust-line)"/>
    <polyline points="275,440 275,476 22,476 22,879 82,879" stroke="var(--authority-line)"/>
    <circle cx="275" cy="440" r="3.5" fill="var(--authority-line)"/>
    <polyline points="335,445 335,482 30,482 30,786 82,786" stroke="var(--experience-line)"/>
    <circle cx="335" cy="445" r="3.5" fill="var(--experience-line)"/>
    <polyline points="395,445 395,488 38,488 38,707 82,707" stroke="var(--expertise-line)"/>
    <circle cx="395" cy="445" r="3.5" fill="var(--expertise-line)"/>
    <polyline points="455,440 455,494 46,494 46,613 82,613" stroke="var(--engagement-line)"/>
    <circle cx="455" cy="440" r="3.5" fill="var(--engagement-line)"/>
    <polyline points="515,430 515,500 54,500 54,520 82,520" stroke="var(--multimedia-line)"/>
    <circle cx="515" cy="430" r="3.5" fill="var(--multimedia-line)"/>
  </svg>

  <section class="breakdown">
    <div class="pillar multimedia">
      <h2 class="pillar-name">MULTIMEDIA:</h2>
      <p class="pillar-text">“Multimedia”consists of infographics, specific images, embedded videos, and other types content aside from the written word. By doing this you provide the same content to audiences that differ based on how they choose to consume content. Online content marketing with multimedia is highly engaging as it presents desired information in a multifaceted but&nbsp; direct and</p>
    </div>
    <div class="pillar engagement">
      <h2 class="pillar-name">ENGAGEMENT:</h2>
      <p class="pillar-text">“Engagement” is essential for views and conversion as it keeps readers locked in on content to the point that they are more likely to move through the website experience and at least consider the value offered in the minutes, hours, days, and weeks that follow their website visit.direct and timely manner.</p>
    </div>
    <div class="pillar expertise">
      <h2 class="pillar-name">EXPERTISE:</h2>
      <p class="pillar-text">“Expertise” refers to the content writer's level of knowledge or skill in a specific subject area that is relevant to the user's search query. High-quality content should be created by someone with relevant expertise in the topic being discussed</p>
    </div>
    <div class="pillar experience">
      <h2 class="pillar-name">EXPERIENCE:</h2>
      <p class="pillar-text">“Experience” in short means that Searchly values firsthand or life experience of the author on the topic a page is about. It is important because often searchers want to know first-hand information before they decide to purchase something or use a certain service.</p>
    </div>
    <div class="pillar authority">
      <h2 class="pillar-name">AUTHORITATIVENESS:</h2>
      <p class="pillar-text">“Authoritativeness” refers to the credibility of the content and the website it is hosted on. Authoritativeness can be established through the quality of the content, the site’s reputation, author’s reputation, external links &amp; content citations, and the credentials of the content creator.</p>
    </div>
    <div class="pillar trust">
      <h2 class="pillar-name">TRUSTWORTHINESS:</h2>
      <p class="pillar-text">““Trustworthiness” is the final result of doing all of the above.&nbsp; If you can write content that is helpful, knowledge, first hand based on experience from someone who is an expert in their field, you get the trust of users consuming your content.&nbsp; If you can gain the user’s trust about your content,&nbsp; Searchly and other search engines will “Trust” you and will provide you with the organic visibility we all strive for..</p>
    </div>
  </section>
</main>
</body>
</html>
```